Sales presentation for Corvel-40

Corvel-40.com is a digital intelligence service which provides news and analysis about digital business models and ecosystems. The readers are C-Suite executives such as chief executive officers, chief marketing officers, chief information officers, strategists, company directors and internet entrepreneurs.

.

Target Market(s)

The audience for the presentation are strategy managers and media buyers at advertising agencies and marketing managers of technology companies and professional service companies.

Industry/Entity Type

Sales

Requirements
Must have
• Slides 9 and 10 have rough diagrams that need to be professionally designed.
Nice to have
• Slide 12 could do with a better piece of generic art

```html
<!DOCTYPE html>
<html lang="en">
<head>
<meta charset="utf-8">
<title>Corvel-40 sales presentation</title>
<link rel="stylesheet" href="https://fonts.googleapis.com/css2?family=Bebas+Neue&family=Oswald:wght@500&family=Roboto:ital,wght@0,400;0,700;1,400&display=swap">
<style>
  :root {
    --ink: #30353b;
    --slate: #5f6b72;
    --sky: #6cc4f0;
    --sky-pale: #cdeefa;
    --text: #333a40;
    --paper: #ffffff;
    --photo-tone: #8a8f94;
  }
  * { margin: 0; padding: 0; box-sizing: border-box; }
  html, body { width: 1200px; height: 1000px; overflow: hidden; background: var(--paper); }
  body { position: relative; font-family: "Roboto", Arial, sans-serif; color: var(--text); }

  .slide {
    position: absolute; left: 308px; width: 585px; height: 439px;
    background: var(--paper); box-shadow: 0 1px 6px rgba(0,0,0,.28);
    overflow: hidden;
  }
  .slide--model { top: 45px; }
  .slide--contributors { top: 516px; }

  .slide__header { position: absolute; left: 0; top: 0; }
  .slide__title {
    position: absolute; right: 26px; top: 14px;
    font-family: "Bebas Neue", "Oswald", sans-serif; font-size: 38px; line-height: 1;
    color: var(--sky); letter-spacing: .5px;
  }

  .slide__footer { position: absolute; left: 0; bottom: 0; width: 585px; height: 50px; }
  .brand {
    position: absolute; left: 14px; top: 390px;
    font-family: "Bebas Neue", "Oswald", sans-serif; font-size: 31px; line-height: 1;
    color: var(--ink); letter-spacing: .3px;
  }
  .footer-band { position: absolute; left: 0; top: 397px; }
  .footer-caption {
    position: absolute; right: 26px; top: 402px;
    font-family: "Oswald", sans-serif; font-weight: 500; font-size: 7.5px; color: var(--paper);
    letter-spacing: .2px;
  }

  .model-points { position: absolute; left: 30px; top: 142px; width: 236px; list-style: none; }
  .model-points li {
    position: relative; padding-left: 0; margin-bottom: 12px;
    font-size: 12px; line-height: 16.5px; text-align: justify; text-indent: 8px;
  }
  .model-points li::before {
    content: ""; position: absolute; left: 0; top: 5px; width: 5px; height: 5px;
    border-radius: 50%; background: var(--sky);
  }
  .model-note { position: absolute; left: 39px; top: 351px; font-size: 8.5px; font-style: italic; }
  .model-wheel { position: absolute; left: 291px; top: 99px; }
  .wheel-label { font-family: "Oswald", sans-serif; font-weight: 500; font-size: 11.5px; fill: var(--ink); }
  .wheel-hub { font-family: "Oswald", sans-serif; font-weight: 500; font-size: 22px; fill: var(--ink); }

  .contributors-lead {
    position: absolute; left: 29px; top: 108px; width: 529px;
    font-size: 19.5px; font-weight: 700; line-height: 23px; color: var(--sky); text-align: justify;
  }
  .contributor { position: absolute; width: 172px; display: flex; gap: 3px; }
  .contributor__photo {
    position: relative; width: 72px; height: 72px; flex: none; overflow: hidden;
    background: linear-gradient(160deg, #b9b2a6, var(--photo-tone) 60%, #55595e);
  }
  .contributor__photo::after {
    content: ""; position: absolute; right: 0; bottom: 0;
    border-style: solid; border-width: 0 0 20px 20px;
    border-color: transparent transparent var(--sky) transparent;
  }
  .contributor__bio { font-size: 6.2px; line-height: 8px; text-align: justify; color: #222; }
  .contributor__name { color: var(--sky); font-weight: 700; }
</style>
</head>
<body>

<section class="slide slide--model">
  <svg class="slide__header" width="585" height="100" viewBox="0 0 585 100" aria-hidden="true">
    <rect x="52" y="0" width="533" height="59" fill="var(--ink)"/>
    <polygon points="0,0 132,0 52,59" fill="var(--slate)"/>
    <polygon points="0,0 52,59 0,98" fill="var(--sky)"/>
    <polygon points="52,59 52,98 0,98" fill="var(--sky-pale)"/>
  </svg>
  <h1 class="slide__title">Halden Model</h1>

  <ul class="model-points">
    <li>The Halden model turns the traditional model around on itself putting the customer at the centre of the conversation.</li>
    <li>The model recognises that customers want to apply their own filters to content.</li>
    <li>By editorialising your content marketing we amplify your story to our readers in a way that engages their interest, matches their workflow and promote share-ability.</li>
  </ul>
  <p class="model-note">In the Halden model customers determine the value of content</p>

  <svg class="model-wheel" width="266" height="266" viewBox="-133 -133 266 266" role="img" aria-label="Content wheel with the customer at the centre">
    <g stroke="#fff" stroke-width="4">
      <path d="M0,-52 L0,-130 A130,130 0 0 1 91.9,-91.9 L36.8,-36.8 A52,52 0 0 0 0,-52Z" fill="#6cc4f0"/>
      <path d="M36.8,-36.8 L91.9,-91.9 A130,130 0 0 1 130,0 L52,0 A52,52 0 0 0 36.8,-36.8Z" fill="#8fd4f5"/>
      <path d="M52,0 L130,0 A130,130 0 0 1 91.9,91.9 L36.8,36.8 A52,52 0 0 0 52,0Z" fill="#b3e1f7"/>
      <path d="M36.8,36.8 L91.9,91.9 A130,130 0 0 1 0,130 L0,52 A52,52 0 0 0 36.8,36.8Z" fill="#d0eefb"/>
      <path d="M0,52 L0,130 A130,130 0 0 1 -91.9,91.9 L-36.8,36.8 A52,52 0 0 0 0,52Z" fill="#7ccbf2"/>
      <path d="M-36.8,36.8 L-91.9,91.9 A130,130 0 0 1 -130,0 L-52,0 A52,52 0 0 0 -36.8,36.8Z" fill="#a6dcf6"/>
      <path d="M-52,0 L-130,0 A130,130 0 0 1 -91.9,-91.9 L-36.8,-36.8 A52,52 0 0 0 -52,0Z" fill="#bfe5f8"/>
      <path d="M-36.8,-36.8 L-91.9,-91.9 A130,130 0 0 1 0,-130 L0,-52 A52,52 0 0 0 -36.8,-36.8Z" fill="#d7f0fb"/>
    </g>
    <g class="wheel-label" text-anchor="middle">
      <text x="36" y="-83">NEWS</text>
      <text x="84" y="-29">FEATURES</text>
      <text x="84" y="38">OPINION</text>
      <text x="38" y="80">GUEST</text><text x="38" y="94">COLUMNS</text>
      <text x="-38" y="80">SPECIAL</text><text x="-38" y="94">REPORTS</text>
      <text x="-84" y="28">CUSTOM</text><text x="-84" y="42">PUBLISHING</text>
      <text x="-84" y="-29">ADVERTORIAL</text>
      <text x="-40" y="-83">ADVERSTISING</text>
    </g>
    <text class="wheel-hub" x="0" y="8" text-anchor="middle">CUSTOMER</text>
  </svg>

  <svg class="footer-band" width="585" height="22" viewBox="0 0 585 22" aria-hidden="true">
    <polygon points="110,11 124,0 585,0 585,22 124,22" fill="var(--sky)"/>
  </svg>
  <p class="brand">Corvel-40</p>
  <p class="footer-caption">TITLE OF THE PRESENTATION - 25/09/2013</p>
</section>

<section class="slide slide--contributors">
  <svg class="slide__header" width="585" height="100" viewBox="0 0 585 100" aria-hidden="true">
    <rect x="52" y="0" width="533" height="59" fill="var(--ink)"/>
    <polygon points="0,0 132,0 52,59" fill="var(--slate)"/>
    <polygon points="0,0 52,59 0,98" fill="var(--sky)"/>
    <polygon points="52,59 52,98 0,98" fill="var(--sky-pale)"/>
  </svg>
  <h1 class="slide__title">Our Contributors</h1>

  <p class="contributors-lead">Corvel-40’s writers are senior industry executives and practitioners with extensive experience building and managing successful businesses online and offline.</p>

  <article class="contributor" style="left:29px; top:191px;">
    <div class="contributor__photo" role="img" aria-label="Portrait photo of Adrian Marlowe"></div>
    <p class="contributor__bio"><span class="contributor__name">Adrian Marlowe</span> is the editor and publisher of Corvel-40. He is a former associate publisher of the National Business Ledger and NBW, deputy managing director of QMG, and editor of The Trade Register.</p>
  </article>
  <article class="contributor" style="left:204px; top:191px;">
    <div class="contributor__photo" role="img" aria-label="Portrait photo of Martin Keale"></div>
    <p class="contributor__bio"><span class="contributor__name">Martin Keale</span> is a counsellor at global business advisory firm Veridan. He was CEO of the Business Ledger Group from 1998 until March 2011.</p>
  </article>
  <article class="contributor" style="left:379px; top:191px;">
    <div class="contributor__photo" role="img" aria-label="Portrait photo of Talia"></div>
    <p class="contributor__bio"><span class="contributor__name">Talia</span> is a Ashbury-educated business professional with a diverse and international background across the full range of media, advocacy, marketing, stakeholder, change and business management.</p>
  </article>
  <article class="contributor" style="left:29px; top:285px;">
    <div class="contributor__photo" role="img" aria-label="Portrait photo of Brianna Holt"></div>
    <p class="contributor__bio"><span class="contributor__name">Brianna Holt</span> is the managing director of Carver Lane in the Australia and Asia-Pacific region, whilst heading up the Carver Lane global media, digital and communications practice.</p>
  </article>
  <article class="contributor" style="left:204px; top:285px;">
    <div class="contributor__photo" role="img" aria-label="Portrait photo of Ted Arden"></div>
    <p class="contributor__bio">After a decade reporting on business technology in the 90s and nodies, <span class="contributor__name">Ted Arden</span> spent the majority of this millennium as an ecommerce professional.</p>
  </article>
  <article class="contributor" style="left:379px; top:285px;">
    <div class="contributor__photo" role="img" aria-label="Portrait photo of Alice Renwick"></div>
    <p class="contributor__bio"><span class="contributor__name">Alice Renwick</span> is a director at Quadrix, a Sydney based analytics and strategy consultancy. She works with businesses to drive value from technology investment and develop effective data driven strategies for marketing and customer engagement.</p>
  </article>

  <svg class="footer-band" width="585" height="22" viewBox="0 0 585 22" aria-hidden="true">
    <polygon points="110,11 124,0 585,0 585,22 124,22" fill="var(--sky)"/>
  </svg>
  <p class="brand">Corvel-40</p>
  <p class="footer-caption">TITLE OF THE PRESENTATION - 25/09/2013</p>
</section>

</body>
</html>
```